Rigboard Media Co Business Card Design

We have a newly created business and logo, but we now need business cards using the new logo.
We are an Australian based business, and we sell advertising space on trucks. The business cards will be seen by media buyers, direct advertisers, fleet owners and business people in general.
Our colours are very simple - black and a strong yellow, with some white. We have chosen the black and yellow for various reasons, but in particular because they are high contrast, and they also have a parallel with the number plates used on our roads, which is relevant to our product offering.
My initial thoughts:
Keep it simple and uncluttered
Use both sides
Our default is Century Gothic
I can provide logo files as required. We do not yet have a website, so I can't direct you there just yet. That may well be another project!
Target Market(s)
The business cards will be seen by media buyers, direct advertisers, fleet owners and business people in general.
Industry/Entity Type
Advertising
Look and feel

```html
<!DOCTYPE html>
<html lang="en">
<head>
<meta charset="utf-8">
<title>Rigboard Media Co – Business Cards</title>
<link rel="stylesheet" href="https://fonts.googleapis.com/css2?family=Rubik:wght@400;500;700;800&display=swap">
<style>
  :root {
    --yellow: #d6dc1c;
    --black: #0a0a0a;
    --white: #f4f4f2;
    --grey: #bdbdbd;
    --backdrop: #e9e6e1;
    --card-w: 540px;
    --card-h: 310px;
  }
  * { box-sizing: border-box; margin: 0; padding: 0; }
  html, body { width: 1200px; height: 880px; overflow: hidden; }
  body {
    background: var(--backdrop);
    font-family: "Rubik", "Century Gothic", sans-serif;
    position: relative;
  }
  .card {
    position: absolute;
    width: var(--card-w);
    height: var(--card-h);
    background: var(--black);
    border-radius: 4px;
    box-shadow: 0 14px 30px rgba(0,0,0,.22);
    overflow: hidden;
  }

  /* Front */
  .card--front { left: 60px; top: 470px; }
  .front-frame {
    position: absolute;
    inset: 18px;
    background: var(--yellow);
    border-radius: 26px;
  }
  .front-panel {
    position: absolute;
    top: 16px; left: 16px; right: 16px; bottom: 44px;
    background: var(--black);
    border-radius: 16px;
    display: flex;
    align-items: center;
    justify-content: center;
    gap: 16px;
  }
  .brand-mark {
    width: 26px; height: 26px;
    background: var(--yellow);
  }
  .brand-name {
    color: var(--yellow);
    font-weight: 800;
    font-size: 38px;
    letter-spacing: 1px;
    text-transform: uppercase;
    line-height: 1;
  }
  .front-web {
    position: absolute;
    left: 0; right: 0; bottom: 12px;
    text-align: center;
    color: var(--black);
    font-weight: 500;
    font-size: 18px;
    letter-spacing: 1.5px;
  }

  /* Back */
  .card--back { left: 600px; top: 110px; }
  .contact { position: absolute; left: 40px; top: 30px; width: 260px; }
  .person-name {
    color: var(--yellow);
    font-weight: 700;
    font-size: 27px;
    line-height: 1.1;
  }
  .person-role {
    color: var(--white);
    font-size: 13px;
    margin-top: 4px;
  }
  .rule {
    height: 2px;
    background: var(--yellow);
    margin: 14px 0 12px;
  }
  .contact-list { list-style: none; }
  .contact-list li {
    display: flex;
    align-items: center;
    gap: 12px;
    color: var(--white);
    font-size: 14px;
    line-height: 1;
    margin-bottom: 8px;
  }
  .icon { width: 13px; height: 13px; flex: none; fill: var(--yellow); }
  .address {
    display: flex;
    gap: 12px;
    color: var(--white);
    font-size: 14px;
    line-height: 1.45;
  }
  .address .icon { margin-top: 3px; }
  .badge {
    position: absolute;
    right: 34px; top: 56px;
    width: 170px; height: 112px;
    background: var(--yellow);
    border-radius: 16px;
    display: flex;
    align-items: center;
    justify-content: center;
    text-align: center;
    padding: 10px;
  }
  .badge-name {
    color: var(--black);
    font-weight: 800;
    font-size: 20px;
    line-height: 1.1;
    text-transform: uppercase;
  }
</style>
</head>
<body>

  <section class="card card--front" aria-label="Business card front">
    <div class="front-frame">
      <div class="front-panel">
        <span class="brand-mark"></span>
        <span class="brand-name">Rigboard Media Co</span>
      </div>
      <p class="front-web">www.rigboard.example</p>
    </div>
  </section>

  <section class="card card--back" aria-label="Business card back">
    <div class="contact">
      <h1 class="person-name">Dale Harper</h1>
      <p class="person-role">Founder</p>
      <div class="rule"></div>
      <ul class="contact-list">
        <li>
          <svg class="icon" viewBox="0 0 16 16" aria-hidden="true"><path d="M3 1h3l1.5 4-2 1.2a9 9 0 0 0 4.3 4.3L11 8.5l4 1.5v3a2 2 0 0 1-2 2A12 12 0 0 1 1 3a2 2 0 0 1 2-2z"/></svg>
          1800 555 019
        </li>
        <li>
          <svg class="icon" viewBox="0 0 16 16" aria-hidden="true"><path d="M4 0h8a1 1 0 0 1 1 1v14a1 1 0 0 1-1 1H4a1 1 0 0 1-1-1V1a1 1 0 0 1 1-1zm1 2v10h6V2zm3 11a1 1 0 1 0 0 2 1 1 0 0 0 0-2z"/></svg>
          +61 4 0000 1234
        </li>
        <li>
          <svg class="icon" viewBox="0 0 16 16" aria-hidden="true"><path d="M0 3h16v10H0zm1.5 1.2v.4L8 9l6.5-4.4v-.4z"/></svg>
          dale@rigboard.example
        </li>
        <li>
          <svg class="icon" viewBox="0 0 16 16" aria-hidden="true"><circle cx="8" cy="8" r="7.5"/></svg>
          www.rigboard.example
        </li>
      </ul>
      <div class="rule"></div>
      <p class="address">
        <svg class="icon" viewBox="0 0 16 16" aria-hidden="true"><path d="M8 0a5.5 5.5 0 0 1 5.5 5.5C13.5 10 8 16 8 16S2.5 10 2.5 5.5A5.5 5.5 0 0 1 8 0zm0 3.3a2.2 2.2 0 1 0 0 4.4 2.2 2.2 0 0 0 0-4.4z"/></svg>
        <span>PO Box 418<br>Kestrel Bay NSW 2999</span>
      </p>
    </div>
    <div class="badge">
      <span class="badge-name">Rigboard Media Co</span>
    </div>
  </section>

</body>
</html>
```